New Agency Branding - Logo & Business Card

Project Description

ZIP is a creative agency that crafts memorable product experiences through meaningful design. By channeling the needs of the business and its customers, we are able to construct solutions that are elegant yet effective, powerful yet playful, and familiar yet stimulating.

In addition to our focus towards creating excellent products, we firmly believe that building a strong company culture is paramount. Our values revolve around building an environment that is passionate, supportive, collaborative, curious, humorous, and healthy. The ZIP team is relatively small, and we intend on keep this family tight-knit. We take great care in deciding who we work with and what we work on.

What we’re looking for is a designer who is willing to take on the challenge of helping us visually define and express the ZIP brand. We must comfortably occupy the consumer, commercial, and enterprise sectors. This means looking professional without sacrificing charm. We’re passionate about design and we care about people.

Deliverables

Logo

The first exercise would be to create the ZIP logo by referencing the concept that is attached (filename: ZIP Concept Logo). We like the idea of utilizing negative space, but are open to other suggestions. In terms of color, we’ve been flirting with the idea of purple as the primary color, but are again open to other explorations. The logo should be bold, professional, playful, and versatile (it should look just as crisp blown up on a website as it would on a contract).

Accepted Format(s): Adobe Illustrator (.ai) 

Business Card

The second exercise would be to design a business card utilizing the logo. The shape can be standard or square (single our double-sided), and must include the following:

• ZIP Logo
• Tagline: "human experiences, designed"
• First and Last Name
• Job Role
• Contact Information (email address and phone number)
• Website URL

In terms of typography, we’d like to see considered pairings that compliment the logo, are legible, and can cohesively translate to other mediums (i.e. the ZIP website).

Accepted Format(s): Adobe Photoshop (.psd) OR Adobe Illustrator (.ai)

Style Guide

Finally, we’d like to have the brand defined and presented in a style guide. This would include the full color palette (primary color, secondary color, etc.) and font usage. In addition, we’d like to see rationale clearly communicated for the decisions made.

Visual References

Companies that inspire us:

morrow+finch
http://www.morrowfinch.example/story/morrow-finch/

BRISK
http://www.briskco.example

NestLoop
https://www.nestloop.example

Fundwheel
https://www.fundwheel.example

Target Market(s)

Startups, Small to Mid Sized Businesses, Consultant Businesses

Industry/Entity Type

Design Agency

Contact Information for Business Card

FRONT: ZIP LOGO on White background

BACK: Tag line "human experiences, designed", name (i.e. Mark Ellery), job role (i.e. Director, Product Development), phone number, email address, and website. The background color could be a solid color although we are open to suggestions.

Logo Text

ZIP

Font styles to use
Sans Serif

Colors
b768aa
a54499
d2a4cc
876aae
6b449b

Requirements
Must have
• A sense of playfulnesses, charm, excitement, and energy.
• Clean and minimal design
• Avoid using icons for contact information
• NOTE: Not all of the purples that have been chosen must be used. These are only suggestions.

```html
<!DOCTYPE html>
<html lang="en">
<head>
<meta charset="utf-8">
<title>ZIP – Business Cards</title>
<link rel="stylesheet" href="https://fonts.googleapis.com/css2?family=Open+Sans:wght@400;600;700;800&display=swap">
<style>
  :root {
    --bg: #e9e6e3;
    --card-white: #f4f4f5;
    --card-grey: #dcdcde;
    --purple: #6b449b;
    --purple-light: #876aae;
    --magenta: #a54499;
    --magenta-light: #b768aa;
    --ink: #4a4a4c;
    --white: #ffffff;
  }
  * { margin: 0; padding: 0; box-sizing: border-box; }
  html, body { width: 1200px; height: 900px; overflow: hidden; }
  body {
    background: var(--bg);
    font-family: "Open Sans", Arial, sans-serif;
    display: flex;
    align-items: center;
    justify-content: center;
    gap: 40px;
  }
  .card {
    position: relative;
    width: 540px;
    height: 310px;
    overflow: hidden;
    background: linear-gradient(135deg, var(--card-white) 0%, #e9e9eb 60%, var(--card-grey) 100%);
    box-shadow: 0 2px 3px rgba(0,0,0,.12), 0 10px 24px rgba(0,0,0,.12);
  }

  /* Contact side */
  .card-back .name-panel {
    position: absolute;
    left: 0; top: 0;
    width: 330px; height: 176px;
    background: linear-gradient(160deg, var(--purple-light), var(--purple));
    clip-path: polygon(0 0, 40% 0, 100% 100%, 0 100%);
  }
  .card-back .person {
    position: absolute;
    left: 30px; top: 114px;
    color: var(--white);
  }
  .person-name { font-size: 23px; font-weight: 700; line-height: 1.1; }
  .person-role { font-size: 12px; font-weight: 400; letter-spacing: .06em; margin-top: 2px; }
  .card-back .wordmark {
    position: absolute;
    right: 70px; top: 22px;
    font-size: 50px; font-weight: 800;
    color: var(--ink);
    letter-spacing: -.02em;
    line-height: 1;
  }
  .contact-band {
    position: absolute;
    left: 0; right: 0; top: 184px;
    height: 50px;
    background: linear-gradient(90deg, var(--purple-light), var(--magenta) 55%, var(--magenta-light));
    border-top: 4px solid var(--card-white);
    border-bottom: 4px solid var(--card-white);
    box-shadow: 0 -3px 0 var(--magenta), 0 3px 0 var(--magenta);
    display: flex;
    justify-content: space-between;
    align-items: center;
    padding: 0 28px;
  }
  .contact-list { list-style: none; color: var(--white); font-size: 12.5px; line-height: 19px; }
  .contact-list.right { text-align: right; }
  .address {
    position: absolute;
    left: 0; right: 30px; top: 262px;
    text-align: right;
    font-size: 14px;
    color: var(--ink);
  }

  /* Logo side */
  .card-front { background: linear-gradient(180deg, var(--card-white), #e4e4e6 45%); }
  .card-front .lower-field {
    position: absolute;
    left: 0; right: 0; bottom: 0;
    height: 55%;
    background: linear-gradient(160deg, var(--purple-light), var(--purple));
  }
  .card-front .wordmark {
    position: absolute;
    left: 0; right: 0; top: 62px;
    text-align: center;
    font-size: 78px; font-weight: 800;
    color: var(--purple);
    letter-spacing: -.02em;
    line-height: 1;
  }
  .card-front .tagline {
    position: absolute;
    left: 0; right: 0; top: 200px;
    text-align: center;
    font-size: 15px; font-weight: 400;
    letter-spacing: .08em;
    color: var(--white);
  }
</style>
</head>
<body>
  <article class="card card-back" aria-label="Business card, contact side">
    <div class="name-panel"></div>
    <div class="person">
      <p class="person-name">Corin Alvedo</p>
      <p class="person-role">PRESIDENT</p>
    </div>
    <p class="wordmark">ZIP</p>
    <div class="contact-band">
      <ul class="contact-list">
        <li>0000 000 000</li>
        <li>info@yourcompanymail.com</li>
      </ul>
      <ul class="contact-list right">
        <li>www.yourwebsite.com</li>
        <li>your_social</li>
      </ul>
    </div>
    <p class="address">48 Harbor Point RD Ventana, CA 90000</p>
  </article>

  <article class="card card-front" aria-label="Business card, logo side">
    <div class="lower-field"></div>
    <p class="wordmark">ZIP</p>
    <p class="tagline">human experiences, designed</p>
  </article>
</body>
</html>
```